Business card for hedge fund
Vornelle Capital Management
Project: Business card for hedge fund
Business card for hedge fund - Financial Services
Creative Brief
Professional
Wanrudee Halvorsen
Chief Operating Officer
wanru.halvorsen@vornellecap.example
2 additional names: Martin Gaskell, Portfolio Manager p: +1-555-382-4719 e-mail: martin.gaskell@vornellecap.example Jia Luo, Portfolio Manager p: +852-5123-9046 e: jia.luo@vornellecap.example No address to be included

```html
<!DOCTYPE html>
<html lang="en">
<head>
<meta charset="utf-8">
<title>Vornelle Capital Management — Business Card</title>
<link href="https://fonts.googleapis.com/css2?family=Open+Sans:wght@400;600;700&display=swap" rel="stylesheet">
<style>
  :root {
    --page-bg: #e7e4df;
    --card-white: #ffffff;
    --panel-dark: #3b3c3e;
    --panel-mid: #56575a;
    --accent-orange: #f39a1e;
    --accent-gold: #f7b733;
    --text-light: #f2f2f2;
    --text-muted: #c9c9c9;
    --logo-ink: #3a3a3a;
  }
  html, body {
    margin: 0;
    width: 1200px;
    height: 914px;
    overflow: hidden;
    background: var(--page-bg);
    font-family: "Open Sans", Arial, sans-serif;
  }
  .business-card {
    position: absolute;
    left: 75px;
    top: 157px;
    width: 1050px;
    height: 600px;
    background: var(--card-white);
    box-shadow: 0 6px 24px rgba(0,0,0,0.18);
    overflow: hidden;
  }
  .card-shapes {
    position: absolute;
    inset: 0;
  }
  .holder {
    position: absolute;
    left: 70px;
    top: 40px;
    color: var(--text-light);
  }
  .holder-name {
    margin: 0;
    font-size: 22px;
    font-weight: 700;
  }
  .holder-title {
    margin: 4px 0 0;
    font-size: 15px;
    color: var(--text-muted);
  }
  .contact-list {
    position: absolute;
    left: 30px;
    top: 340px;
    margin: 0;
    padding: 0;
    list-style: none;
    color: var(--text-light);
    font-size: 17px;
  }
  .contact-item {
    display: flex;
    align-items: center;
    height: 37px;
  }
  .contact-icon {
    width: 26px;
    height: 26px;
    margin-right: 14px;
    flex: none;
  }
  .brand-name {
    position: absolute;
    left: 500px;
    top: 245px;
    width: 500px;
    margin: 0;
    text-align: center;
    color: var(--logo-ink);
    font-weight: 400;
    line-height: 1.05;
  }
  .brand-main {
    display: block;
    font-size: 66px;
    letter-spacing: 4px;
  }
  .brand-sub {
    display: block;
    font-size: 24px;
    letter-spacing: 5px;
    margin-top: 6px;
  }
</style>
</head>
<body>
  <div class="business-card">
    <svg class="card-shapes" width="1050" height="600" viewBox="0 0 1050 600">
      <defs>
        <radialGradient id="panelShade" cx="0.35" cy="0.4" r="0.8">
          <stop offset="0" stop-color="var(--panel-mid)"/>
          <stop offset="1" stop-color="var(--panel-dark)"/>
        </radialGradient>
        <linearGradient id="accentBand" x1="0" y1="0" x2="0" y2="1">
          <stop offset="0" stop-color="var(--accent-gold)"/>
          <stop offset="0.5" stop-color="var(--accent-orange)"/>
          <stop offset="1" stop-color="var(--accent-gold)"/>
        </linearGradient>
      </defs>
      <path class="accent-band" d="M335,0 Q505,300 395,600 L380,600 Q470,300 320,0 Z" fill="url(#accentBand)"/>
      <path class="dark-panel" d="M0,0 H320 Q470,300 380,600 H0 Z" fill="url(#panelShade)"/>
      <path class="accent-line" d="M350,0 Q525,300 410,600" fill="none" stroke="var(--accent-orange)" stroke-width="2"/>
    </svg>

    <div class="holder">
      <p class="holder-name">Wanrudee Halvorsen</p>
      <p class="holder-title">Chief Operating Officer</p>
    </div>

    <ul class="contact-list">
      <li class="contact-item">
        <svg class="contact-icon" viewBox="0 0 26 26"><circle cx="13" cy="13" r="13" fill="#fff"/><path d="M9 7 L11 7 L12 10 L10.5 11 Q12 14 15 15.5 L16 14 L19 15 L19 17 Q18 19 16 19 Q8 17 7 9 Q7 7 9 7 Z" fill="var(--panel-dark)"/></svg>
        +1-555-204-6631
      </li>
      <li class="contact-item">
        <svg class="contact-icon" viewBox="0 0 26 26"><circle cx="13" cy="13" r="13" fill="#fff"/><rect x="9" y="6" width="8" height="14" rx="1.5" fill="var(--panel-dark)"/><rect x="10.5" y="8" width="5" height="8" fill="#fff"/></svg>
        +1-555-317-0482
      </li>
      <li class="contact-item">
        <svg class="contact-icon" viewBox="0 0 26 26"><circle cx="13" cy="13" r="13" fill="#fff"/><rect x="7" y="11" width="12" height="8" rx="1" fill="var(--panel-dark)"/><rect x="9" y="6" width="8" height="5" fill="var(--panel-dark)"/></svg>
        +1-555-908-1157
      </li>
      <li class="contact-item">
        <svg class="contact-icon" viewBox="0 0 26 26"><circle cx="13" cy="13" r="13" fill="#fff"/><rect x="6.5" y="8.5" width="13" height="9" fill="var(--panel-dark)"/><path d="M6.5 8.5 L13 14 L19.5 8.5" fill="none" stroke="#fff" stroke-width="1.2"/></svg>
        wanru.halvorsen@vornellecap.example
      </li>
      <li class="contact-item">
        <svg class="contact-icon" viewBox="0 0 26 26"><circle cx="13" cy="13" r="13" fill="#fff"/><circle cx="13" cy="13" r="6.5" fill="none" stroke="var(--panel-dark)" stroke-width="1.5"/><ellipse cx="13" cy="13" rx="2.8" ry="6.5" fill="none" stroke="var(--panel-dark)" stroke-width="1.2"/><line x1="6.5" y1="13" x2="19.5" y2="13" stroke="var(--panel-dark)" stroke-width="1.2"/></svg>
        www.vornellecap.example
      </li>
    </ul>

    <h1 class="brand-name">
      <span class="brand-main">VORNELLE</span>
      <span class="brand-sub">CAPITAL MANAGEMENT</span>
    </h1>
  </div>
</body>
</html>
```